I need a label design to go on our jars of honey. Our company is called Marlowe Honey Co. The type of honey is called Ridgefern Gold Honey. The jars are 1kg. Attached is the label size. Left hand side needs to have nutritional info... as attached. Middle section is our company name, honey type, 1kg & Harlow Bay, NZ. Right hand side needs to have info as per photo (raw honey etc). I would like to upload more pictures... but I’m unsure how to do this? Thanks, Carol

Target Market(s)

Honey consumers... families

Industry/Entity Type

Food Production

Colors

Designer to choose colors to be used in the design.

Requirements
Must have
• Nutritional info as per upload
• Type of honey & company name as per upload
• 1kg
• Address
Nice to have
• Similar fonts to upload.
• Possibly background image... floral or beach... very faint though.

```html
<!DOCTYPE html>
<html lang="en">
<head>
<meta charset="utf-8">
<title>Marlowe Honey Co. – Ridgefern Gold Honey label</title>
<link rel="stylesheet" href="https://fonts.googleapis.com/css2?family=Open+Sans:wght@400;600;700&family=Kaushan+Script&family=Patrick+Hand&family=Gochi+Hand&display=swap">
<style>
  :root {
    --berry: #b13561;
    --berry-deep: #8a1a42;
    --berry-edge: #7a1238;
    --ink: #ffffff;
    --bloom-pink: #e0338f;
    --bloom-orange: #f07a4a;
    --bloom-violet: #9a3c9c;
    --leaf: #5fc7a6;
  }
  * { box-sizing: border-box; margin: 0; padding: 0; }
  html, body { width: 1200px; height: 608px; overflow: hidden; background: var(--berry-deep); }
  .label {
    position: relative; width: 1200px; height: 608px; overflow: hidden; color: var(--ink);
    background: radial-gradient(ellipse 60% 75% at 50% 45%, var(--berry) 0%, #a02a54 55%, var(--berry-edge) 100%);
  }
  .bg-pattern {
    position: absolute; inset: 0;
    background: radial-gradient(circle at 15% 85%, rgba(255,255,255,.05), transparent 30%),
                radial-gradient(circle at 85% 20%, rgba(255,255,255,.05), transparent 30%);
  }
  .bloom { position: absolute; border-radius: 46% 54% 50% 50%; }
  .bloom--top {
    left: 610px; top: 30px; width: 262px; height: 196px;
    background: radial-gradient(circle at 60% 45%, var(--bloom-orange) 0%, var(--bloom-pink) 35%, var(--bloom-violet) 60%, rgba(95,199,166,.55) 78%, transparent 92%);
  }
  .bloom--bottom {
    left: 290px; top: 342px; width: 122px; height: 218px;
    background: radial-gradient(ellipse at 50% 50%, var(--bloom-orange) 0%, var(--bloom-pink) 35%, var(--bloom-violet) 60%, rgba(95,199,166,.55) 78%, transparent 94%);
  }

  /* left column */
  .panel-left { position: absolute; left: 47px; top: 56px; width: 241px; font-family: "Open Sans", sans-serif; }
  .origin { text-align: center; font-size: 16px; line-height: 20px; }
  .nutrition { margin-top: 12px; border: 1.5px solid var(--ink); padding: 0 6px 8px; font-size: 11.5px; }
  .nutrition h2 { font-size: 15px; font-weight: 600; text-align: center; padding: 5px 0 4px; border-bottom: 1.5px solid var(--ink); }
  .servings { font-weight: 600; padding: 5px 0 6px; border-bottom: 1px solid var(--ink); line-height: 15px; }
  .nutrition table { width: 100%; border-collapse: collapse; font-weight: 600; }
  .nutrition th { font-size: 10px; text-align: left; padding: 6px 0; border-bottom: 1px solid var(--ink); }
  .nutrition td { padding: 2.5px 0; }
  .nutrition tr.first td { padding-top: 9px; }
  .storage { margin-top: 26px; text-align: center; font-size: 15.5px; line-height: 20px; }
  .batch { position: absolute; left: 49px; top: 487px; width: 239px; height: 77px; border: 1.5px solid var(--ink);
    font-family: "Open Sans", sans-serif; font-weight: 600; font-size: 14px; line-height: 20px; padding: 7px 9px; }

  /* centre */
  .brand-name { position: absolute; left: 390px; top: 104px; width: 420px; text-align: center;
    font-family: "Open Sans", sans-serif; font-weight: 600; font-size: 36px; line-height: 44px; }
  .product-name { position: absolute; left: 340px; top: 252px; width: 520px; text-align: center;
    font-family: "Kaushan Script", cursive; font-weight: 400; font-size: 60px; line-height: 66px; }
  .weight, .place { position: absolute; left: 440px; width: 300px; text-align: center; font-family: "Gochi Hand", cursive; }
  .weight { top: 462px; font-size: 58px; line-height: 62px; }
  .place { top: 524px; font-size: 34px; line-height: 40px; }

  /* right */
  .panel-right { position: absolute; left: 900px; top: 82px; width: 260px; text-align: center;
    font-family: "Patrick Hand", cursive; font-size: 18.5px; line-height: 24.5px; }
  .panel-right p + p { margin-top: 23px; }
  .panel-right .blessing { margin-top: 46px; }
  .contact { position: absolute; left: 900px; top: 462px; width: 260px; text-align: center; font-style: normal;
    font-family: "Patrick Hand", cursive; font-size: 18px; line-height: 24.5px; }
</style>
</head>
<body>
<main class="label">
  <div class="bg-pattern" role="img" aria-label="Faint tropical floral pattern across the label background"></div>
  <div class="bloom bloom--top" role="img" aria-label="Cluster of pink and orange hibiscus flowers with teal leaves"></div>
  <div class="bloom bloom--bottom" role="img" aria-label="Cluster of pink and orange hibiscus flowers with teal leaves"></div>

  <section class="panel-left">
    <p class="origin">100% New Zeland Honey<br>No added ingredients</p>
    <div class="nutrition">
      <h2>NUTRITIONAL INFORMATION</h2>
      <p class="servings">Servings per package: 100<br>Serving size: 10g</p>
      <table>
        <tr><th>Average Quantity</th><th>per Serving</th><th>per 100g</th></tr>
        <tr class="first"><td>Energy</td><td>134kj</td><td>1340kj</td></tr>
        <tr><td>Protein</td><td>0.04g</td><td>0.4g</td></tr>
        <tr><td>Fat total</td><td>0g</td><td>0g</td></tr>
        <tr><td>&nbsp;- saturated</td><td>0g</td><td>0g</td></tr>
        <tr><td>Carbohydrate</td><td>7.9g</td><td>79g</td></tr>
        <tr><td>&nbsp;- sugars</td><td>7.8g</td><td>78.1g</td></tr>
        <tr><td>Sodium</td><td>1.2mg</td><td>12mg</td></tr>
      </table>
    </div>
    <p class="storage">Store upright in a cool, dry place.<br>No refrigeration needed.<br>Not recomended for infants<br>below the age of 12 months.</p>
  </section>
  <div class="batch">Best before:<br>RMP:<br>Batch No:</div>

  <h1 class="brand-name">Marlowe Honey Co.</h1>
  <h2 class="product-name">Ridgefern<br>Gold Honey</h2>
  <p class="weight">1kg</p>
  <p class="place">Harlow Bay, NZ</p>

  <section class="panel-right">
    <p>Sourced from the beautiful<br>Coromandel Peninsula.</p>
    <p>Our honey comes to you raw &amp;<br>unpasteurised, ensured it retains<br>all the natural goodness!</p>
    <p>Arohanui,<br>Owen, Carol &amp; boys</p>
    <p class="blessing">'Marlowe' - all thanks to God for<br>His incredible creation!</p>
  </section>
  <address class="contact">www.marlowehoney.co.nz<br>42 Kauri Lane<br>Harlow Bay<br>New Zeland</address>
</main>
</body>
</html>
```